Graphic Banner Design - 2.5' x 6' - High Tech Company

We are in need of a banner design for an outdoor sign that will be used at sponsorship events.

Size
2.5' x 6'

The company is a high tech company, and the design will be used for action sports events. So lining up to that would be good.

Tag line to be incorporated...
"Extreme IT Services for Extreme Needs."

Target Market(s)

Business Owners, Entrepreneurs, IT Professionals.

Industry/Entity Type

Information Technology

Logo Text

Vexlora

Colors

Designer to choose colors to be used in the design.

Requirements
Must have
• Must feel young and vibrant, fit in to an action sports event and just be out of this world awesome.
• In the world of the IT, we are the Zanverolli. Fast, Awesome, not necessarily cheap, but you know it will do what you want extremely well. Not for everyone, but always desired.

```html
<!DOCTYPE html>
<html lang="en">
<head>
<meta charset="utf-8">
<title>Vexlora – Event Banner</title>
<link href="https://fonts.googleapis.com/css2?family=Montserrat:wght@400;500&display=swap" rel="stylesheet">
<style>
  :root {
    --page-bg: #f8f8f8;
    --stage-black: #03040c;
    --stage-navy: #0e1460;
    --stage-blue: #2f3fd8;
    --stage-violet: #5a3ad6;
    --stage-glow: #b9d4ff;
    --stage-cyan: #7fd0f0;
    --stage-red: #e0344f;
    --band-light: rgba(255, 255, 255, 0.2);
    --text-white: #ffffff;
  }
  html, body {
    margin: 0;
    width: 1200px;
    height: 394px;
    overflow: hidden;
    background: var(--page-bg);
  }
  .banner {
    position: absolute;
    left: 85px;
    top: 74px;
    width: 1031px;
    height: 247px;
    overflow: hidden;
    font-family: "Montserrat", sans-serif;
    color: var(--text-white);
  }
  .concert-photo {
    position: absolute;
    inset: 0;
    background:
      radial-gradient(ellipse 14% 40% at 72% 30%, rgba(230, 240, 255, 0.95) 0%, rgba(185, 212, 255, 0.5) 40%, transparent 75%),
      radial-gradient(ellipse 10% 45% at 88% 20%, rgba(220, 235, 255, 0.85) 0%, transparent 75%),
      radial-gradient(ellipse 9% 40% at 42% 15%, rgba(200, 225, 255, 0.7) 0%, transparent 75%),
      radial-gradient(ellipse 6% 10% at 34% 78%, rgba(230, 240, 255, 0.8) 0%, transparent 80%),
      radial-gradient(ellipse 5% 9% at 80% 72%, rgba(230, 240, 255, 0.75) 0%, transparent 80%),
      radial-gradient(ellipse 8% 8% at 28% 83%, rgba(224, 52, 79, 0.6) 0%, transparent 80%),
      radial-gradient(ellipse 7% 12% at 60% 50%, rgba(224, 52, 79, 0.45) 0%, transparent 80%),
      radial-gradient(ellipse 18% 50% at 97% 50%, rgba(127, 208, 240, 0.55) 0%, transparent 75%),
      radial-gradient(ellipse 30% 60% at 30% 45%, var(--stage-violet) 0%, transparent 75%),
      radial-gradient(ellipse 35% 60% at 62% 60%, var(--stage-blue) 0%, transparent 80%),
      linear-gradient(180deg, var(--stage-navy) 0%, var(--stage-blue) 50%, #1a1f6a 78%, var(--stage-black) 100%);
  }
  .concert-photo::before {
    content: "";
    position: absolute;
    inset: 0;
    background: linear-gradient(90deg, var(--stage-black) 0%, rgba(3, 4, 12, 0.55) 14%, transparent 34%);
  }
  .concert-photo::after {
    content: "";
    position: absolute;
    left: 0;
    right: 0;
    bottom: 0;
    height: 28%;
    background: linear-gradient(180deg, transparent 0%, rgba(3, 4, 12, 0.8) 100%);
  }
  .graphics {
    position: absolute;
    inset: 0;
    width: 100%;
    height: 100%;
  }
  .brand-name {
    position: absolute;
    left: 96px;
    top: 21px;
    margin: 0;
    font-size: 24px;
    font-weight: 500;
    letter-spacing: 0.4px;
    line-height: 30px;
  }
  .tagline {
    position: absolute;
    right: 39px;
    top: 201px;
    margin: 0;
    font-size: 17.5px;
    font-weight: 400;
    line-height: 22px;
    white-space: nowrap;
  }
</style>
</head>
<body>
  <section class="banner">
    <div class="concert-photo" role="img" aria-label="Concert photo: band performing on stage under bright blue spotlights with a cheering crowd in front"></div>
    <svg class="graphics" viewBox="0 0 1289 309" preserveAspectRatio="none" aria-hidden="true">
      <defs>
        <radialGradient id="medallion-fill" cx="50%" cy="55%" r="55%">
          <stop offset="0%" stop-color="#4a3ad0" stop-opacity="0.75"/>
          <stop offset="45%" stop-color="#1a1c70" stop-opacity="0.85"/>
          <stop offset="100%" stop-color="#03040c" stop-opacity="0.95"/>
        </radialGradient>
        <radialGradient id="medallion-spot" cx="55%" cy="70%" r="30%">
          <stop offset="0%" stop-color="#e0344f" stop-opacity="0.5"/>
          <stop offset="100%" stop-color="#e0344f" stop-opacity="0"/>
        </radialGradient>
      </defs>
      <polygon class="light-band" points="594,0 1289,0 780,309 90,309" fill="var(--band-light)"/>
      <polygon class="shade-band" points="1289,0 1289,309 780,309" fill="rgba(0,0,30,0.18)"/>
      <circle class="medallion" cx="644" cy="155" r="122" fill="url(#medallion-fill)"/>
      <circle class="medallion-glow" cx="644" cy="155" r="122" fill="url(#medallion-spot)"/>
    </svg>
    <h1 class="brand-name">Vexlora</h1>
    <p class="tagline">Extreme IT Services for Extreme Needs</p>
  </section>
</body>
</html>
```